Hadley & Partners, LLC Business Card 2016

We need a new business card design for a very important trade show coming up.

We are a compliance Consulting Firm. Our clients are stock brokerage firms and investment advisers.

I would like our logo on both sides of the card.

Info in the front of the card shold include:

Logo
First & Last Name
Title
Office #
Cell #
Email
Company Address (42 W. Calloway St., Suite 300 Larkfield, OR 91417

Back of the card should include the logo and url: www.hadleypartnersgroup.com

Target Market(s)

Stock Brokerage Firms and Investment Advisers

Industry/Entity Type

Financial Service

Contact Information for Business Card

Marcus J. Pellew
President
42 W. Calloway St., Suite 300
Larkfield, OR 91417
O 626.555.0147 ext. 204
C 818.555.0193
Email: marcus@hadleypartnersgroup.com
www.hadleypartnersgroup.com

Requirements
Nice to have
• The back of the card could be black with the logo with the white letters.
• I do want the front of the card to at least have the color logo with the black "Hadley & Partners Lettering.

```html
<!DOCTYPE html>
<html lang="en">
<head>
<meta charset="utf-8">
<title>Hadley &amp; Partners — Business Card</title>
<link rel="stylesheet" href="https://fonts.googleapis.com/css2?family=Roboto:wght@400;500&family=Saira+Condensed:wght@600&display=swap">
<style>
  :root {
    --backdrop: #161616;
    --card: #232323;
    --ink: #ffffff;
    --ink-soft: #e6e6e6;
    --red: #e5392f;
    --red-deep: #a71c16;
    --steel-light: #b3b8bd;
    --steel-dark: #424a52;
    --rule: #bfbfbf;
  }
  * { margin: 0; padding: 0; box-sizing: border-box; }
  html, body {
    width: 1200px; height: 1158px; overflow: hidden;
    background: var(--backdrop);
    font-family: "Roboto", Arial, sans-serif;
    color: var(--ink);
  }
  .card {
    position: absolute; left: 248px; width: 736px; height: 435px;
    background: var(--card); overflow: hidden;
  }
  .card--back { top: 77px; }
  .card--front { top: 610px; }

  .brand { position: absolute; display: flex; align-items: center; }
  .brand__mark { background: var(--red); flex: none; }
  .brand__name { font-family: "Roboto", Arial, sans-serif; font-weight: 400; color: var(--ink); white-space: nowrap; letter-spacing: 1px; }

  .card--back .brand { left: 0; right: 0; top: 186px; justify-content: center; gap: 22px; }
  .card--back .brand__mark { width: 60px; height: 60px; }
  .card--back .brand__name { font-size: 52px; }

  .card--front .brand { left: 37px; top: 64px; gap: 16px; }
  .card--front .brand__mark { width: 46px; height: 46px; }
  .card--front .brand__name { font-size: 38px; }

  .person { position: absolute; right: 37px; top: 192px; text-align: right; }
  .person__name { font-family: "Saira Condensed", "Arial Narrow", sans-serif; font-weight: 600; font-size: 31px; line-height: 34px; }
  .person__title { font-size: 18px; line-height: 22px; color: var(--ink-soft); }
  .person-rule { position: absolute; left: 37px; top: 246px; width: 573px; height: 1px; background: var(--rule); }

  .contacts { position: absolute; left: 37px; top: 275px; list-style: none; }
  .contacts li { display: flex; align-items: center; height: 26px; font-size: 19px; color: var(--ink-soft); }
  .contacts svg { width: 19px; height: 17px; margin-right: 18px; fill: var(--ink); }

  .address { position: absolute; right: 37px; top: 288px; text-align: right; font-size: 19px; line-height: 26px; color: var(--ink-soft); font-style: normal; }

  .band-steel { position: absolute; left: 0; top: 412px; width: 420px; height: 23px; background: linear-gradient(90deg, var(--steel-light), var(--steel-dark)); }
  .band-red {
    position: absolute; left: 372px; top: 384px; width: 364px; height: 51px;
    background: linear-gradient(90deg, var(--red), var(--red-deep));
    clip-path: polygon(32px 0, 100% 0, 100% 100%, 0 100%);
  }
  .band-red__url { position: absolute; right: 37px; top: 397px; font-size: 19px; line-height: 24px; color: var(--ink); }
</style>
</head>
<body>
  <section class="card card--back">
    <div class="brand">
      <span class="brand__mark"></span>
      <span class="brand__name">Hadley &amp; Partners</span>
    </div>
  </section>

  <section class="card card--front">
    <div class="brand">
      <span class="brand__mark"></span>
      <span class="brand__name">Hadley &amp; Partners</span>
    </div>

    <div class="person">
      <p class="person__name">Marcus J. Pellew</p>
      <p class="person__title">President</p>
    </div>
    <div class="person-rule"></div>

    <ul class="contacts">
      <li>
        <svg viewBox="0 0 18 16" aria-hidden="true"><path d="M1 5c0-2 3-3 8-3s8 1 8 3v2h-4V5.5H5V7H1z"/><rect x="3" y="8" width="12" height="7" rx="1"/></svg>
        541.555.0147 ext. 204
      </li>
      <li>
        <svg viewBox="0 0 18 16" aria-hidden="true"><path d="M9 1a7 7 0 1 0 0 14A7 7 0 0 0 9 1zm0 1.5c.8 0 1.8 1.6 2.1 4.5H6.9C7.2 4.1 8.2 2.5 9 2.5zM3.6 7c.2-1.8 1.2-3.2 2.6-4-.4 1-.7 2.4-.8 4zm8.9 0c-.1-1.6-.4-3-.8-4 1.4.8 2.4 2.2 2.6 4zM3.6 9h1.8c.1 1.6.4 3 .8 4-1.4-.8-2.4-2.2-2.6-4zm3.3 0h4.2c-.3 2.9-1.3 4.5-2.1 4.5S7.2 11.9 6.9 9zm5.7 0h1.8c-.2 1.8-1.2 3.2-2.6 4 .4-1 .7-2.4.8-4z"/></svg>
        971.555.0193
      </li>
      <li>
        <svg viewBox="0 0 18 16" aria-hidden="true"><path d="M1 3h16v10H1zm1.5 1.2v.3L9 9l6.5-4.5v-.3zM2.5 6.3v5.5h13V6.3L9 10.8z"/></svg>
        marcus@hadleypartnersgroup.com
      </li>
    </ul>

    <address class="address">
      42 W. Calloway St., Suite 300<br>
      Larkfield, OR 97417
    </address>

    <div class="band-steel"></div>
    <div class="band-red"></div>
    <p class="band-red__url">hadleypartnersgroup.com</p>
  </section>
</body>
</html>
```